Visitenkarten-Design für ein Beratungsunternehmen im Immobilienbereich
Zielgruppe
Wir sind ein Beratungsunternehmen im Immobilienbereich. Von der Planung, Ingenieuring, bis hin zum Vertriebskonzept
Aufgabenstellung
Das vorhandene Logo mit den zugehörigen Farben und Schriften
Firmennamen: FALKOR
Name: Georg Tannhuber
Geschäftsführer
Anschrift: Lindenweg 14, 64799 Tannwiesen
What3word: ///kerze.wolken.tanzen
Telefon: +49 6299 4710582
Mobil: +49 162 5083716
Mail: kontakt@falkor-beispiel.immo
Web: www.falkor-beispiel.immo
Slogan: Werte, die bleiben
Das Logo soll als Prägung und teilweise in silber/ heissfolie ausgeführt werden.

```html
<!DOCTYPE html>
<html lang="de">
<head>
<meta charset="utf-8">
<title>FALKOR Visitenkarten</title>
<link rel="stylesheet" href="https://fonts.googleapis.com/css2?family=Source+Sans+3:wght@400;600;700&family=Montserrat:wght@500;600&display=swap">
<style>
:root{
  --navy:#2c3262;
  --text-grey:#555559;
  --border:#b9b9bd;
  --silver-dark:#67666b;
  --silver-light:#d4d4d8;
  --paper:#ffffff;
}
*{box-sizing:border-box;margin:0;padding:0}
html,body{width:1200px;height:1200px;overflow:hidden;background:var(--paper)}
.sheet{position:relative;width:1200px;height:1200px}
.card{position:absolute;left:360px;width:481px;height:312px;border:1px solid var(--border);background:var(--paper);overflow:hidden;font-family:"Source Sans 3",sans-serif}
.card--front{top:244px}
.card--variant{top:645px}
.brand-name{position:absolute;right:22px;top:20px;font-family:"Montserrat",sans-serif;font-weight:600;font-size:49px;letter-spacing:3px;color:var(--navy);line-height:1}
.person{position:absolute;left:22px;top:100px}
.person__name{font-weight:600;font-size:23px;color:var(--navy);letter-spacing:-0.2px;line-height:1.2}
.person__role{font-size:15px;color:var(--text-grey);margin-top:4px}
.contact{position:absolute;left:268px;top:131px;list-style:none}
.contact__item{display:flex;align-items:flex-start;font-size:15px;line-height:20px;color:var(--text-grey)}
.contact__icon{width:16px;height:20px;margin-right:8px;display:flex;align-items:center;justify-content:center;flex:none}
.contact__icon svg{width:13px;height:13px;fill:var(--navy)}
.footer-band{position:absolute;left:0;bottom:0;width:481px;height:38px}
.slogan{position:absolute;right:24px;bottom:9px;font-family:"Montserrat",sans-serif;font-weight:600;font-size:16.5px;letter-spacing:0.6px;line-height:1;white-space:nowrap}
.slogan--silver{background:linear-gradient(90deg,#8d8d93,#e3e3e6 50%,#9a9aa0);-webkit-background-clip:text;background-clip:text;color:transparent}
.slogan--white{color:#fff}
</style>
</head>
<body>
<div class="sheet">

  <section class="card card--front">
    <div class="brand-name">FALKOR</div>
    <div class="person">
      <div class="person__name">Georg Tannhuber</div>
      <div class="person__role">Geschäftsführer</div>
    </div>
    <ul class="contact">
      <li class="contact__item"><span class="contact__icon"><svg viewBox="0 0 24 24"><path d="M12 1a8 8 0 0 0-8 8c0 6 8 14 8 14s8-8 8-14a8 8 0 0 0-8-8zm0 11a3 3 0 1 1 0-6 3 3 0 0 1 0 6z"/></svg></span><span>Lindenweg 14<br>64799 Tannwiesen</span></li>
      <li class="contact__item"><span class="contact__icon"><svg viewBox="0 0 24 24"><path d="M6.6 10.8a15 15 0 0 0 6.6 6.6l2.2-2.2a1 1 0 0 1 1-.25 11.4 11.4 0 0 0 3.6.6 1 1 0 0 1 1 1V20a1 1 0 0 1-1 1A17 17 0 0 1 3 4a1 1 0 0 1 1-1h3.5a1 1 0 0 1 1 1c0 1.25.2 2.45.6 3.6a1 1 0 0 1-.25 1z"/></svg></span><span>+49 6299 4710582</span></li>
      <li class="contact__item"><span class="contact__icon"><svg viewBox="0 0 24 24"><path d="M7 1h10a2 2 0 0 1 2 2v18a2 2 0 0 1-2 2H7a2 2 0 0 1-2-2V3a2 2 0 0 1 2-2zm0 3v14h10V4zm5 15.5a1 1 0 1 0 0 2 1 1 0 0 0 0-2z"/></svg></span><span>+49 162 5083716</span></li>
      <li class="contact__item"><span class="contact__icon"><svg viewBox="0 0 24 24"><path d="M2 5h20v2l-10 6L2 7zm0 4l10 6 10-6v10H2z"/></svg></span><span>kontakt@falkor-beispiel.immo</span></li>
      <li class="contact__item"><span class="contact__icon"><svg viewBox="0 0 24 24"><path d="M12 2a10 10 0 1 0 0 20 10 10 0 0 0 0-20zm6.9 6h-2.9a15 15 0 0 0-1.4-3.6A8 8 0 0 1 18.9 8zM12 4c.8 1.2 1.5 2.5 1.9 4h-3.8c.4-1.5 1.1-2.8 1.9-4zM4.3 14a8 8 0 0 1 0-4h3.4a16 16 0 0 0 0 4zm.8 2h2.9a15 15 0 0 0 1.4 3.6A8 8 0 0 1 5.1 16zM8 8H5.1a8 8 0 0 1 4.3-3.6A15 15 0 0 0 8 8zm4 12c-.8-1.2-1.5-2.5-1.9-4h3.8c-.4 1.5-1.1 2.8-1.9 4zm2.3-6H9.7a14 14 0 0 1 0-4h4.6a14 14 0 0 1 0 4zm.3 5.6A15 15 0 0 0 16 16h2.9a8 8 0 0 1-4.3 3.6zm1.7-5.6a16 16 0 0 0 0-4h3.4a8 8 0 0 1 0 4z"/></svg></span><span>www.falkor-beispiel.immo</span></li>
    </ul>
    <svg class="footer-band" viewBox="0 0 481 38" aria-hidden="true">
      <defs><linearGradient id="silverA" x1="0" x2="1"><stop offset="0" stop-color="#67666b"/><stop offset="1" stop-color="#d4d4d8"/></linearGradient></defs>
      <polygon points="0,10 212,10 202,38 0,38" fill="url(#silverA)"/>
      <polygon points="220,0 481,0 481,38 205,38" fill="#2c3262"/>
    </svg>
    <div class="slogan slogan--silver">WERTE, DIE BLEIBEN</div>
  </section>

  <section class="card card--variant">
    <div class="brand-name">FALKOR</div>
    <div class="person">
      <div class="person__name">Georg Tannhuber</div>
      <div class="person__role">Geschäftsführer</div>
    </div>
    <ul class="contact">
      <li class="contact__item"><span class="contact__icon"><svg viewBox="0 0 24 24"><path d="M12 1a8 8 0 0 0-8 8c0 6 8 14 8 14s8-8 8-14a8 8 0 0 0-8-8zm0 11a3 3 0 1 1 0-6 3 3 0 0 1 0 6z"/></svg></span><span>Lindenweg 14<br>64799 Tannwiesen</span></li>
      <li class="contact__item"><span class="contact__icon"><svg viewBox="0 0 24 24"><path d="M6.6 10.8a15 15 0 0 0 6.6 6.6l2.2-2.2a1 1 0 0 1 1-.25 11.4 11.4 0 0 0 3.6.6 1 1 0 0 1 1 1V20a1 1 0 0 1-1 1A17 17 0 0 1 3 4a1 1 0 0 1 1-1h3.5a1 1 0 0 1 1 1c0 1.25.2 2.45.6 3.6a1 1 0 0 1-.25 1z"/></svg></span><span>+49 6299 4710582</span></li>
      <li class="contact__item"><span class="contact__icon"><svg viewBox="0 0 24 24"><path d="M7 1h10a2 2 0 0 1 2 2v18a2 2 0 0 1-2 2H7a2 2 0 0 1-2-2V3a2 2 0 0 1 2-2zm0 3v14h10V4zm5 15.5a1 1 0 1 0 0 2 1 1 0 0 0 0-2z"/></svg></span><span>+49 162 5083716</span></li>
      <li class="contact__item"><span class="contact__icon"><svg viewBox="0 0 24 24"><path d="M2 5h20v2l-10 6L2 7zm0 4l10 6 10-6v10H2z"/></svg></span><span>kontakt@falkor-beispiel.immo</span></li>
      <li class="contact__item"><span class="contact__icon"><svg viewBox="0 0 24 24"><path d="M12 2a10 10 0 1 0 0 20 10 10 0 0 0 0-20zm6.9 6h-2.9a15 15 0 0 0-1.4-3.6A8 8 0 0 1 18.9 8zM12 4c.8 1.2 1.5 2.5 1.9 4h-3.8c.4-1.5 1.1-2.8 1.9-4zM4.3 14a8 8 0 0 1 0-4h3.4a16 16 0 0 0 0 4zm.8 2h2.9a15 15 0 0 0 1.4 3.6A8 8 0 0 1 5.1 16zM8 8H5.1a8 8 0 0 1 4.3-3.6A15 15 0 0 0 8 8zm4 12c-.8-1.2-1.5-2.5-1.9-4h3.8c-.4 1.5-1.1 2.8-1.9 4zm2.3-6H9.7a14 14 0 0 1 0-4h4.6a14 14 0 0 1 0 4zm.3 5.6A15 15 0 0 0 16 16h2.9a8 8 0 0 1-4.3 3.6zm1.7-5.6a16 16 0 0 0 0-4h3.4a8 8 0 0 1 0 4z"/></svg></span><span>www.falkor-beispiel.immo</span></li>
    </ul>
    <svg class="footer-band" viewBox="0 0 481 38" aria-hidden="true">
      <defs><linearGradient id="silverB" x1="0" x2="1"><stop offset="0" stop-color="#67666b"/><stop offset="1" stop-color="#d4d4d8"/></linearGradient></defs>
      <polygon points="0,10 212,10 202,38 0,38" fill="url(#silverB)"/>
      <polygon points="220,0 481,0 481,38 205,38" fill="#2c3262"/>
    </svg>
    <div class="slogan slogan--white">WERTE, DIE BLEIBEN</div>
  </section>

</div>
</body>
</html>
```